Tess Hallard Communication business card

I am starting a small, country-based business that offers writing, communication and marketing services to a wide range of clients, inner city big business, to mining, through to agriculture.

The appeal of my business is that it's mobile and flexible. It's just me, with lots of hands-on experience on construction and infrastructure projects.

I can provide the following services:

• Communication planning and management
• Issues and media management
• Marketing and communication materials
• Project management and strategy
• Government liaison
• Incident management communication
• Stakeholder management

It would be great to be able to use the elements of the business card design on other stationery.

Industry/Entity Type

Communication

Requirements
Must have
• The following information:

Tess Hallard
M: 0427 391 806
E: tess@thcommsample.com

PO Box 52
Tarrabool Q 4291
Nice to have
• a rural element (windmill, workboots, wheat stalk)

```html
<!DOCTYPE html>
<html lang="en">
<head>
<meta charset="utf-8">
<title>Tess Hallard Communication – Business Card</title>
<link href="https://fonts.googleapis.com/css2?family=Tenor+Sans&display=swap" rel="stylesheet">
<style>
  :root {
    --page-bg: #ffffff;
    --card-ink: #5b5756;
    --foil: #f2f2f0;
  }
  html, body {
    margin: 0;
    padding: 0;
    width: 1200px;
    height: 900px;
    overflow: hidden;
    background: var(--page-bg);
  }
  .stationery {
    position: relative;
    width: 1200px;
    height: 900px;
  }
  .card {
    position: absolute;
    top: 115px;
    width: 433px;
    height: 668px;
    background: var(--card-ink);
  }
  .card--front { left: 107px; }
  .card--back { left: 647px; }
  .card svg {
    display: block;
    width: 433px;
    height: 668px;
  }
  .card text {
    font-family: "Tenor Sans", "Optima", sans-serif;
    fill: var(--foil);
  }
  .rule {
    stroke: var(--foil);
    fill: none;
  }
  .mark-dot { fill: var(--foil); }
</style>
</head>
<body>
<main class="stationery">

  <section class="card card--front" aria-label="Card front">
    <svg viewBox="0 0 433 668" xmlns="http://www.w3.org/2000/svg">
      <g class="brand-mark">
        <line class="rule" x1="69" y1="120" x2="165" y2="120" stroke-width="3"/>
        <circle class="mark-dot" cx="214" cy="120" r="9"/>
        <line class="rule" x1="265" y1="120" x2="363" y2="120" stroke-width="3"/>
      </g>
      <g class="wordmark">
        <line class="rule" x1="69" y1="201" x2="363" y2="201" stroke-width="1.2"/>
        <line class="rule" x1="69" y1="205" x2="363" y2="205" stroke-width="1.2"/>
        <text class="wordmark__name" x="69" y="245" font-size="40" textLength="294" lengthAdjust="spacingAndGlyphs">TESS HALLARD</text>
        <text class="wordmark__trade" x="69" y="273" font-size="27" textLength="294" lengthAdjust="spacingAndGlyphs">COMMUNICATION</text>
        <line class="rule" x1="69" y1="279" x2="363" y2="279" stroke-width="1.2"/>
        <line class="rule" x1="69" y1="283" x2="363" y2="283" stroke-width="1.2"/>
      </g>
      <line class="rule footer-rule" x1="69" y1="615" x2="361" y2="615" stroke-width="1.5"/>
    </svg>
  </section>

  <section class="card card--back" aria-label="Card back">
    <svg viewBox="0 0 433 668" xmlns="http://www.w3.org/2000/svg">
      <g class="contact">
        <line class="rule" x1="69" y1="396" x2="363" y2="396" stroke-width="1.2"/>
        <text class="contact__name" x="69" y="433" font-size="40" textLength="294" lengthAdjust="spacingAndGlyphs">TESS HALLARD</text>
        <text class="contact__phone" x="69" y="462" font-size="29" textLength="294" lengthAdjust="spacing">0427 391 806</text>
        <text class="contact__email" x="69" y="482" font-size="20" textLength="294" lengthAdjust="spacingAndGlyphs">tess@thcommsample.com</text>
        <line class="rule" x1="69" y1="491" x2="363" y2="491" stroke-width="1.2"/>
        <line class="rule" x1="69" y1="495" x2="363" y2="495" stroke-width="1.2"/>
      </g>
      <g class="address">
        <text class="address__box" x="69" y="537" font-size="40" textLength="294" lengthAdjust="spacing">PO BOX 52</text>
        <text class="address__town" x="69" y="563" font-size="29" textLength="294" lengthAdjust="spacingAndGlyphs">TARRABOOL Q 4291</text>
        <line class="rule" x1="69" y1="574" x2="363" y2="574" stroke-width="1.2"/>
        <line class="rule" x1="69" y1="578" x2="363" y2="578" stroke-width="1.2"/>
      </g>
      <g class="signoff">
        <text class="signoff__trade" x="69" y="600" font-size="15" textLength="294" lengthAdjust="spacingAndGlyphs">TESS HALLARD COMMUNICATION</text>
        <line class="rule" x1="69" y1="605" x2="363" y2="605" stroke-width="1.2"/>
      </g>
    </svg>
  </section>

</main>
</body>
</html>
```